Expanding the consciousness of Humanity - Solvane-Harbor

Please note that whoever will win this project , a 1on1 Powerpoint design project will separately be launched and will be offered to the winning designer.

---------
This letterhead is to provide proposals, as well as manuals for my clients.

I am looking for the letter, power point design and business card that inspires people when they see it, that they feel that design has been done with love and passion. Something that is professional, simple and yet creative, Business like, yet spiritual. That inspires growth!

This part of the branding for my company, therefore the business card as well as the power point design that will come after as 1on1 project should have the same team and feeling.

Solvane harbor, The company will be providing Coaching services (one-one or groups) to corporations, teams and individuals, partnering with them to achieve their goals/vision, by helping them to remove the self-imposed limiting beliefs, helping them to get them out of their own way, helping them to raise their level of consciousness and self-awareness.

The vision is: Bring conscious leadership to the workplace and to individuals for the wellbeing of humanity.

I know that somewhere out there will resonate with this, and will be inspired to provide the best design :) thank you very much!!!!!

MPORTANT:
- To use Free Fonts - let me know where I can download them
- Editable formats please for the double sized business card

LOGO is attached in pdf. If needed other file type please let me know

Thank you thank you in advance for your time and inspiration!! Sending good vibes for a great design out there

Must Have:
- Please keep on mind that the cards - power point will have the same feeling - Corporate branding
- that is not to heavy to look at it, that is simple and beautiful and inspiring
- Looking to have Calibri or Calibri light font

imple, yet inspirational - Professional, yet playful - business like, yet spiritual

I am looking for something different that the "standard" designs out there.

For example, the Logo of the company in the back side with a quote and the front side something simple, yet inspiring. that has the contact info as well as the social media details LinkedIn - Facebook - tweeter - website

Open for suggestions and inspiration :)

Thank you!

Font styles to use
Sans Serif

Requirements
Must have
• - Please keep on mind that the cards - power point will have the same feeling
• - Corporate branding
• - that is not to heavy to look at it, that is simple and beautiful and inspiring
• - Looking to have Calibri or Calibri light font
• - Corporate colours as the logo

```html
<!DOCTYPE html>
<html lang="en">
<head>
<meta charset="utf-8">
<title>Solvane-Harbor Stationery</title>
<link rel="stylesheet" href="https://fonts.googleapis.com/css2?family=Carlito:wght@400;700&display=swap">
<style>
:root{
  --blue:#1d4f8c;
  --blue-deep:#0b4c8b;
  --yellow:#fbbb14;
  --white:#ffffff;
  --ink:#1d3f6e;
  --stage:#c6c6c8;
  --stage-light:#d6d6d7;
  --faint-blue:rgba(255,255,255,.09);
}
*{margin:0;padding:0;box-sizing:border-box}
html,body{width:1200px;height:1063px;overflow:hidden}
body{font-family:"Carlito",sans-serif;background:linear-gradient(90deg,var(--stage) 0%,#d0d0d2 50%,var(--stage) 100%);position:relative;color:var(--ink)}
.band-light{position:absolute;left:0;top:468px;width:1112px;height:278px;background:var(--stage-light)}
.piece{position:absolute;overflow:hidden;box-shadow:0 1px 4px rgba(0,0,0,.18)}
.brand{display:flex;align-items:center;gap:6px;white-space:nowrap}
.brand-dot{border-radius:50%;background:var(--blue);flex:none}
.brand-name{color:var(--yellow);text-transform:uppercase;font-weight:400;letter-spacing:.02em}
.brand.on-blue .brand-dot{background:var(--white)}
.brand.on-blue .brand-name{color:var(--white)}
.emblem-faint{position:absolute;border-radius:50%}

/* letterhead */
.letterhead{left:78px;top:19px;width:344px;height:437px;background:var(--white)}
.letterhead .brand{position:absolute;left:34px;top:19px}
.letterhead .brand-dot{width:30px;height:30px}
.letterhead .brand-name{font-size:9px}
.letterhead .contact{position:absolute;right:30px;top:30px;display:flex;gap:6px;font-size:5px;line-height:6px;color:#333}
.letterhead .contact .addr{text-align:right;border-right:1px solid var(--blue);padding-right:5px}
.letterhead .emblem-faint{left:72px;top:150px;width:190px;height:190px;background:radial-gradient(circle,#fbeccc 0 45%,#e3e3ee 46% 100%);opacity:.8}
.letterhead .footer{position:absolute;left:0;bottom:0;width:100%;height:12px;background:var(--blue);color:var(--white);font-size:5px;text-align:center;line-height:12px}

/* folder */
.folder{left:456px;top:23px;width:652px;height:433px;background:var(--blue-deep)}
.folder .pocket{position:absolute;left:325px;top:0;width:327px;height:164px;background:var(--white);display:flex;align-items:center;justify-content:center}
.folder .pocket .brand-dot{width:62px;height:62px}
.folder .pocket .brand-name{font-size:15px}
.folder .stripe{position:absolute;left:325px;top:164px;width:327px;height:12px;background:var(--yellow)}
.folder .emblem-faint{left:380px;top:190px;width:245px;height:245px;background:rgba(40,110,170,.55)}

/* cards */
.card-back{left:317px;top:531px;width:266px;height:164px;background:var(--blue);display:flex;align-items:center;justify-content:center}
.card-back .brand-dot{width:48px;height:48px}
.card-back .brand-name{font-size:11px}
.card-front{left:627px;top:531px;width:270px;height:164px;background:var(--white)}
.card-front .brand{position:absolute;left:70px;top:22px}
.card-front .brand-dot{width:44px;height:44px}
.card-front .brand-name{font-size:9px}
.card-front .details{position:absolute;left:40px;top:86px;display:flex;gap:6px;font-size:8px;line-height:9.5px;color:#1a1a1a}
.card-front .person{text-align:right;border-right:1px solid var(--blue);padding-right:5px}
.card-front .person .name{color:var(--blue);text-transform:uppercase}
.card-front .person .title{color:var(--yellow)}
.card-front .lines li{list-style:none;display:flex;align-items:center;gap:3px}
.card-front .lines svg{width:6px;height:6px;flex:none}
.card-front .footer{position:absolute;left:0;bottom:0;width:100%;height:7px;background:var(--blue)}

/* slides */
.slide{top:756px;width:323px;height:248px;background:var(--white)}
.slide-title{left:87px}
.slide-chart{left:442px}
.slide-end{left:794px;width:325px}
.slide .hero{position:absolute;left:0;top:0;width:100%;height:143px;background:var(--blue);overflow:hidden}
.slide .hero h2{position:absolute;left:21px;top:70px;font-size:19px;font-weight:400;color:var(--yellow);letter-spacing:.02em}
.slide-end .hero h2{top:66px;left:31px}
.slide .hero .emblem-faint{right:-20px;top:-10px;width:170px;height:170px;background:var(--faint-blue)}
.slide .brand{position:absolute}
.slide .brand-dot{width:36px;height:36px}
.slide .brand-name{font-size:8px}
.slide-title .brand{left:182px;top:188px}
.slide-title .web{position:absolute;left:228px;top:214px;font-size:5px;color:#333}
.slide-end .brand{left:182px;top:188px}
.slide-end .contact{position:absolute;left:16px;top:225px;font-size:4.5px;line-height:6px;color:#333}
.slide .bar{position:absolute;bottom:0;height:8px}
.slide .bar.b{left:0;width:223px;background:var(--blue)}
.slide .bar.y{right:0;width:98px;background:var(--yellow)}
.slide-chart .brand{left:26px;top:20px}
.slide-chart .brand-dot{width:26px;height:26px}
.slide-chart .brand-name{font-size:6px}
.slide-chart .heading{position:absolute;right:21px;top:28px;font-size:9px;color:var(--blue);text-transform:uppercase}
.slide-chart svg.chart{position:absolute;left:0;top:0}
.slide-chart .rule{position:absolute;left:15px;top:224px;width:296px;height:2px;background:var(--blue)}
.slide-chart .web{position:absolute;right:21px;top:232px;font-size:5px;color:#333}
</style>
</head>
<body>
<div class="band-light"></div>

<section class="piece letterhead">
  <div class="brand"><span class="brand-dot"></span><span class="brand-name">Solvane-Harbor</span></div>
  <div class="contact">
    <div class="addr">2150 Lakeview Ave, Ste 400<br>Harborton, WA 98112</div>
    <div>555 210 4400<br>555 210 4400</div>
  </div>
  <div class="emblem-faint" role="img" aria-label="Faint brand emblem decoration"></div>
  <div class="footer">www.solvaneharbor.com</div>
</section>

<section class="piece folder">
  <div class="pocket"><div class="brand"><span class="brand-dot"></span><span class="brand-name">Solvane-Harbor</span></div></div>
  <div class="stripe"></div>
  <div class="emblem-faint" role="img" aria-label="Faint brand emblem decoration"></div>
</section>

<section class="piece card-back">
  <div class="brand on-blue"><span class="brand-dot"></span><span class="brand-name">Solvane-Harbor</span></div>
</section>

<section class="piece card-front">
  <div class="brand"><span class="brand-dot"></span><span class="brand-name">Solvane-Harbor</span></div>
  <div class="details">
    <div class="person">
      <div class="name">Employee Name</div>
      <div class="title">Title</div>
      <div>2150 Lakeview Ave, Ste 400</div>
      <div>Harborton, WA 98112</div>
    </div>
    <ul class="lines">
      <li><svg viewBox="0 0 6 6"><rect width="6" height="6" rx="1" fill="#fbbb14"/></svg>555 210 4400</li>
      <li><svg viewBox="0 0 6 6"><rect width="6" height="6" rx="1" fill="#fbbb14"/></svg>555 210 4400</li>
      <li><svg viewBox="0 0 6 6"><rect width="6" height="6" rx="1" fill="#fbbb14"/></svg>hello@solvaneharbor.com</li>
      <li><svg viewBox="0 0 6 6"><circle cx="3" cy="3" r="3" fill="#fbbb14"/></svg>www.solvaneharbor.com</li>
    </ul>
  </div>
  <div class="footer"></div>
</section>

<section class="piece slide slide-title">
  <div class="hero"><h2>TITLE GOES HERE</h2><div class="emblem-faint" role="img" aria-label="Faint brand emblem decoration"></div></div>
  <div class="brand"><span class="brand-dot"></span><span class="brand-name">Solvane-Harbor</span></div>
  <div class="web">www.solvaneharbor.com</div>
  <div class="bar b"></div><div class="bar y"></div>
</section>

<section class="piece slide slide-chart">
  <div class="brand"><span class="brand-dot"></span><span class="brand-name">Solvane-Harbor</span></div>
  <div class="heading">Title Goes Here</div>
  <svg class="chart" width="323" height="248" viewBox="0 0 323 248" font-family="Carlito, sans-serif">
    <g stroke="#e6e6e6" stroke-width=".5">
      <line x1="30" y1="82" x2="300" y2="82"/><line x1="30" y1="105" x2="300" y2="105"/>
      <line x1="30" y1="128" x2="300" y2="128"/><line x1="30" y1="151" x2="300" y2="151"/>
      <line x1="30" y1="174" x2="300" y2="174"/>
    </g>
    <line x1="30" y1="186" x2="302" y2="186" stroke="#999" stroke-width=".6"/>
    <line x1="30" y1="82" x2="30" y2="186" stroke="#999" stroke-width=".6"/>
    <g font-size="4" fill="#888" text-anchor="middle">
      <text x="30" y="193">0</text><text x="68.6" y="193">1</text><text x="107.1" y="193">2</text><text x="145.7" y="193">3</text>
      <text x="184.3" y="193">4</text><text x="222.9" y="193">5</text><text x="261.4" y="193">6</text><text x="300" y="193">7</text>
      <text x="165" y="199">Title Goes Here</text>
      <text x="22" y="134" transform="rotate(-90 22 134)">Title Goes Here</text>
    </g>
    <g fill="none" stroke-width="1">
      <polyline stroke="#1d6fb8" points="30,186 68.6,174.4 107.1,162.9 145.7,174.4 184.3,139.8 222.9,162.9 261.4,151.3 300,128.2"/>
      <polyline stroke="#17a593" points="30,172.1 68.6,162.9 107.1,157.1 145.7,151.3 184.3,157.1 222.9,139.8 261.4,162.9 300,116.6"/>
      <polyline stroke="#8cba3e" points="30,160.6 68.6,151.3 107.1,145.5 145.7,145.5 184.3,134 222.9,134 261.4,128.2 300,93.5"/>
      <polyline stroke="#f08a1c" points="30,162.9 68.6,145.5 107.1,139.8 145.7,116.6 184.3,128.2 222.9,145.5 261.4,110.9 300,93.5"/>
    </g>
    <g font-size="4" text-anchor="middle" fill="#333">
      <circle cx="86" cy="152" r="8" fill="#fff" stroke="#1d6fb8" stroke-width="2"/><text x="86" y="153.5">50%</text>
      <circle cx="153" cy="131" r="8" fill="#fff" stroke="#17a593" stroke-width="2"/><text x="153" y="132.5">80%</text>
      <circle cx="219" cy="116" r="8" fill="#fff" stroke="#8cba3e" stroke-width="2"/><text x="219" y="117.5">70%</text>
      <circle cx="286" cy="77" r="8" fill="#fff" stroke="#f08a1c" stroke-width="2"/><text x="286" y="78.5">70%</text>
    </g>
    <g font-size="4" fill="#888">
      <line x1="100" y1="208" x2="108" y2="208" stroke="#1d6fb8"/><text x="110" y="209.5">Series 1</text>
      <line x1="132" y1="208" x2="140" y2="208" stroke="#17a593"/><text x="142" y="209.5">Series 2</text>
      <line x1="164" y1="208" x2="172" y2="208" stroke="#8cba3e"/><text x="174" y="209.5">Series 3</text>
      <line x1="196" y1="208" x2="204" y2="208" stroke="#f08a1c"/><text x="206" y="209.5">Series 4</text>
    </g>
  </svg>
  <div class="rule"></div>
  <div class="web">www.solvaneharbor.com</div>
</section>

<section class="piece slide slide-end">
  <div class="hero"><h2>THANK YOU!</h2><div class="emblem-faint" role="img" aria-label="Faint brand emblem decoration"></div></div>
  <div class="brand"><span class="brand-dot"></span><span class="brand-name">Solvane-Harbor</span></div>
  <div class="contact">555 210 4400 &nbsp; 555 210 4400 &nbsp; www.solvaneharbor.com<br>2150 Lakeview Ave, Ste 400 Harborton, WA 98112</div>
  <div class="bar b"></div><div class="bar y"></div>
</section>
</body>
</html>
```